Zielgruppe
Wir sind eine Wäscherei.
Zielgruppe: Kunden aus der Hotel- und Gastronomiebranche
Aufgabenstellung
Wir benötigen einen 2-seitigen Flyer DIN lang. 9,8 x21cm
TextInhalte sind in der Vorlage-Datei.
Bilder sind eingefügt.

```html
<!DOCTYPE html>
<html lang="de">
<head>
<meta charset="utf-8">
<title>Wäscherei Brandau – Flyer DIN lang</title>
<link href="https://fonts.googleapis.com/css2?family=Roboto:wght@300;400;500;700&display=swap" rel="stylesheet">
<style>
  :root {
    --magenta: #e5007d;
    --sky: #93bde6;
    --sky-light: #d6e6f7;
    --ink: #1d1d1b;
    --band: #f4f6f6;
    --page: #e6e6e6;
    --white: #ffffff;
  }
  * { margin: 0; padding: 0; box-sizing: border-box; }
  html, body { width: 1123px; height: 1200px; overflow: hidden; }
  body {
    background: var(--page);
    font-family: "Roboto", Arial, sans-serif;
    color: var(--ink);
    position: relative;
  }
  .flyer {
    position: absolute;
    left: 69px;
    width: 986px;
    height: 460px;
    background: var(--white);
    overflow: hidden;
  }
  .flyer--front { top: 103px; }
  .flyer--back { top: 637px; }

  .wave-layer { position: absolute; inset: 0; }

  .brand-name {
    position: absolute;
    font-family: "Roboto", Arial, sans-serif;
    font-weight: 700;
    color: var(--magenta);
    text-transform: uppercase;
    white-space: nowrap;
    transform: translateX(-50%);
  }
  .flyer--front .brand-name { left: 475px; top: 38px; font-size: 22px; }
  .flyer--back .brand-name { left: 404px; top: 32px; font-size: 15px; }

  .photo-ring {
    position: absolute;
    border-radius: 50%;
    background: var(--sky-light);
  }
  .photo {
    position: absolute;
    border-radius: 50%;
  }
  .ring-towels { left: 4px; top: 27px; width: 290px; height: 290px; }
  .photo-towels {
    left: 40px; top: 50px; width: 230px; height: 240px;
    background: radial-gradient(circle at 40% 40%, #f2c12e 0%, #e84a8e 45%, #d9293b 70%, #7cb342 100%);
  }
  .ring-laundry { left: 202px; top: 172px; width: 280px; height: 280px; background: var(--white); border: 14px solid var(--sky-light); }
  .photo-laundry {
    left: 226px; top: 186px; width: 232px; height: 232px;
    background: linear-gradient(180deg, #f3dfc8 0%, #e9c845 28%, #d94a3c 45%, #cfe3e6 60%, #4e4d5c 75%, #f0b6a8 100%);
  }

  .service-list {
    position: absolute;
    left: 550px; top: 93px;
    list-style: none;
    font-size: 19px;
    font-weight: 300;
    line-height: 23.7px;
  }
  .service-list li::before { content: "• "; }

  .contact { position: absolute; left: 550px; top: 365px; }
  .contact-name {
    font-size: 24px; font-weight: 400; color: var(--magenta);
    text-transform: uppercase; letter-spacing: 0.3px; margin-bottom: 4px;
  }
  .contact-line { font-size: 13.5px; font-weight: 400; line-height: 18px; }

  .photo-napkin {
    position: absolute; left: 0; top: 0; width: 196px; height: 460px;
    background: linear-gradient(160deg, #ffffff 0%, #eef0ec 25%, #9cc22b 55%, #7fa81d 80%, #ffffff 100%);
  }
  .grey-band {
    position: absolute; left: 238px; top: 0; width: 105px; height: 460px;
    background: var(--band);
  }
  .offer-title {
    position: absolute; left: 200px; top: 104px;
    font-size: 19px; font-weight: 500; color: var(--magenta);
  }
  .offer-text {
    position: absolute; left: 200px; top: 178px; width: 420px;
    font-size: 18.5px; font-weight: 300; line-height: 24px;
  }
  .offer-text p { margin-bottom: 24px; }

  .price-panel {
    position: absolute; left: 629px; top: 0; width: 357px; height: 460px;
    background: var(--sky);
    padding: 50px 20px 0 25px;
    font-size: 18.5px; font-weight: 300; line-height: 23.5px;
  }
  .price-block { margin-bottom: 23.5px; }
  .price-block strong { font-weight: 500; }
  .price { color: var(--magenta); font-weight: 500; }
  .footnote {
    position: absolute; right: 30px; top: 426px;
    font-size: 12px; font-weight: 400;
  }
</style>
</head>
<body>

  <section class="flyer flyer--front" aria-label="Vorderseite">
    <svg class="wave-layer" viewBox="0 0 986 460" aria-hidden="true">
      <path d="M870 0 Q950 30 986 90 L986 0 Z" fill="var(--sky)"/>
      <path d="M830 0 Q930 20 986 75 L986 70 Q920 15 850 0 Z" fill="var(--sky-light)"/>
      <path d="M0 275 Q120 300 250 240 Q360 160 470 210 Q620 300 760 300 Q880 300 986 275 L986 300 Q880 330 760 330 Q600 330 470 240 Q370 185 260 265 Q140 340 0 295 Z" fill="var(--sky)"/>
      <path d="M0 300 Q150 350 270 280 Q360 220 440 250 Q300 260 250 300 Q140 370 0 320 Z" fill="var(--sky-light)"/>
    </svg>
    <div class="photo-ring ring-towels"></div>
    <div class="photo photo-towels" role="img" aria-label="Foto: bunte aufgerollte Handtücher"></div>
    <div class="photo-ring ring-laundry"></div>
    <div class="photo photo-laundry" role="img" aria-label="Foto: Stapel gefalteter Wäsche in Händen"></div>

    <div class="brand-name">Wäscherei Brandau</div>

    <ul class="service-list">
      <li>Serviettenfaltservice – ab November 2017</li>
      <li>Hotel- und Gastronomiewäsche</li>
      <li>Schmutzmatten</li>
      <li>Gardinenservice</li>
      <li>Berufskleidung</li>
      <li>Private Wäsche</li>
      <li>Verkauf von Hotel- und Gastronomietextilien</li>
    </ul>

    <address class="contact" style="font-style:normal">
      <div class="contact-name">Wäscherei Brandau</div>
      <div class="contact-line">Lindenweg 14 | 70000 Musterstadt</div>
      <div class="contact-line">tel. +49 (0) 7000 / 12 34 56</div>
      <div class="contact-line">E-Mail: info@waescherei-brandau.de</div>
    </address>
  </section>

  <section class="flyer flyer--back" aria-label="Rückseite">
    <div class="grey-band"></div>
    <div class="photo-napkin" role="img" aria-label="Foto: grüne Stoffserviette mit Gabel und Messer"></div>
    <div class="brand-name">Wäscherei Brandau</div>

    <h2 class="offer-title">Ihr Serviettenfaltservice • ab November 2017</h2>
    <div class="offer-text">
      <p>Wir optimieren Ihren Serviettenfaltprozess.</p>
      <p>Wir entlasten Sie von dieser demotivierenden und unproduktiven Tätigkeit.</p>
      <p>Wir falten Ihnen Ihre Stoffservietten oder unsere Mietservietten vor.</p>
      <p>Hygienisch, zuverlässig und wirtschaftlich – bereit für die Mise en Place.</p>
    </div>

    <div class="price-panel">
      <div class="price-block">Faltformen – Kategorie 1:<br><strong>Welle, Kerze, Fächer</strong><br>je Faltung für nur <span class="price">0,20 €</span> *</div>
      <div class="price-block">Faltformen – Kategorie 2:<br><strong>Pyramide, Bischofsmütze</strong><br>je Faltung für nur <span class="price">0,35 €</span> *</div>
      <div class="price-block">Weitere Formen sind auf Anfrage möglich. Bei Bedarf stellen wir Ihnen Mietservietten für nur <span class="price">0,25 €</span>* je Stück zur Verfügung. Mindestabnahmemenge: 100 Stück</div>
      <div class="footnote">*zzgl. gesetzliche MwSt.</div>
    </div>
  </section>

</body>
</html>
```